Wordpress Design Project for Skip Hire company

Redgum Skip Hire is a Skip Hire company based in the Western Suburbs of Melbourne (Australia) and was established in 1995.
The colours of the Redgum Skip Hire logo are Pantone 188C (Burgundy) and 424C (Grey). We would like the site to include these colours throughout the site.

The current Redgum Skip Hire site (www.redgumskiphire.example.au) has been in operation for a number of years and as we have recently commenced a project to update the Logo and Corporate ID, a new Website is also appropriate.

The Redgum Skip Hire site only needs to be a simple site and is unlikely to consist of more than 20 pages. The site is primarily used for people to find our contact details, delivery areas and the measurements/size of of the bins we hire to our customers.

Industry/Entity Type

It Company

Requirements
Must have
• A contact page template (which sends an email) which can be used for a main contact page as well as long form response pages to enhance our 'call to action'
A separate enquiry/order form with configurable options will also be required.
A category (products) page will be required which will list all of our bins, a configurable excerpt of the page contents along with a single photo of each bin (a slider may be used also).
We also require the ability for potential customers to look each bin on it's own page as well as a large image, information about each bin and our terms and conditions.
We would also like configurable titles and meta code for each page.
The site will also need the ability to integrate with Trackwell Stats.

```html
<!DOCTYPE html>
<html lang="en">
<head>
<meta charset="utf-8">
<title>Redgum Skip Hire</title>
<link href="https://fonts.googleapis.com/css2?family=PT+Serif:wght@400;700&family=Arimo:wght@400;700&family=Questrial&display=swap" rel="stylesheet">
<style>
:root{
  --burgundy:#8c1208;
  --burgundy-dark:#5e0a04;
  --grey:#6f6f73;
  --text:#444;
  --light:#ececec;
  --line:#d6d6d6;
  --footer:#7b7b7d;
  --footer-top:#58585a;
  --blue:#3b6fb0;
}
*{margin:0;padding:0;box-sizing:border-box}
html,body{width:1053px;height:1200px;overflow:hidden;background:#fff;font-family:"Arimo",Arial,sans-serif;color:var(--text)}
.page{position:relative;width:1053px;height:1200px}
.abs{position:absolute}

.brand{left:78px;top:34px;font-family:"PT Serif",Georgia,serif;font-weight:700;font-size:30px;line-height:34px;color:var(--burgundy);width:200px;display:flex;align-items:center;gap:8px}
.brand .mark{width:14px;height:14px;background:var(--grey);flex:none}

.nav{top:52px;display:flex}
.nav-item{position:absolute;top:0;border-left:1px dotted #bbb;padding-left:8px;height:38px;white-space:nowrap}
.nav-item b{display:block;font-family:"PT Serif",Georgia,serif;font-size:14px;color:#555;letter-spacing:.2px}
.nav-item span{display:block;font-size:10.5px;color:var(--burgundy);margin-top:3px}

.band{left:0;top:131px;width:1053px;height:321px;background:linear-gradient(#6e0b05,#8c1208 40%,#8c1208)}
.slider{left:78px;top:153px;width:897px;height:325px;border:2px solid #fff;border-radius:6px;background:linear-gradient(135deg,#8a7a6a,#c9c2b8 45%,#a9a49a 70%,#d4d2cc);overflow:hidden}
.dots{left:96px;top:452px;display:flex;gap:6px}
.dot{width:15px;height:15px;border-radius:50%;background:#222;border:2px solid #ddd}
.dot.on{background:#38a8e0}

.tagline{left:0;top:495px;width:1053px;text-align:center;font-family:"Questrial",sans-serif;font-size:25px;color:#555}
.rule{left:82px;height:1px;width:890px;background:var(--line)}

.tabs-box{left:86px;top:564px;width:877px;height:261px;border:1px solid var(--burgundy)}
.tab-list{position:absolute;left:0;top:0;width:288px;height:259px;background:var(--light)}
.tab{height:65px;display:flex;align-items:center;justify-content:center;font-family:"PT Serif",Georgia,serif;font-size:15.5px;color:var(--burgundy);border-bottom:1px solid #fff}
.tab.active{background:var(--burgundy);color:#fff}
.tab-copy{position:absolute;left:312px;top:50px;width:269px;font-size:13.4px;line-height:19.2px;text-align:justify;color:#555;letter-spacing:.3px}
.btn-more{position:absolute;left:312px;top:178px;width:155px;height:30px;border:1px solid #ccc;border-radius:3px;background:linear-gradient(#fff,#e9e9e9);font-size:12px;color:var(--blue);padding:8px 12px;display:flex;justify-content:space-between}
.truck{position:absolute;left:602px;top:32px;width:265px;height:198px;border:3px solid #e4e4e4;background:linear-gradient(#8fb0d6 0%,#c7d6e6 40%,#9a9a92 60%,#6d6d68)}

.col-title{font-family:"PT Serif",Georgia,serif;font-size:16px;color:#333;padding-bottom:6px;border-bottom:1px dashed #ccc}
.social{left:94px;top:870px;width:248px}
.follow{display:flex;align-items:center;gap:8px;margin-top:10px;font-size:11px;color:#333}
.follow .ico{width:35px;height:35px;border-radius:7px}
.newsletter{left:96px;top:990px;width:251px}
.newsletter .col-title{font-family:"Arimo",Arial,sans-serif;font-weight:700;font-size:15px}
.field{border:1px solid #ccc;border-radius:2px;height:28px;font-size:9px;letter-spacing:1px;color:#aaa;padding:9px 11px;background:#fff}
.btn-blue{width:138px;height:28px;border-radius:3px;background:linear-gradient(#4c86c6,#245ea0);color:#fff;font-family:"PT Serif",Georgia,serif;font-size:12px;padding:6px 10px;display:flex;justify-content:space-between;box-shadow:0 1px 0 #1b4a80}
.touch{left:396px;top:870px;width:251px}
.contact{left:701px;top:868px;width:251px}
.contact dl{margin-top:12px;margin-left:6px;font-size:10.5px;line-height:14.4px;color:#555;display:grid;grid-template-columns:50px auto}
.contact dd{margin:0}
.accept{font-size:11.5px;color:#333;margin-top:22px;padding-bottom:6px;border-bottom:1px dashed #ccc}
.cards{display:flex;gap:3px;margin:12px 0 0 56px}
.card{width:58px;height:38px;border:1px solid #999;display:flex;align-items:center;justify-content:center;font-size:11px;font-weight:700;color:var(--burgundy);background:#fff}

.footer{left:0;top:1105px;width:1053px;height:95px;background:var(--footer);border-top:9px solid var(--footer-top)}
.footer-links{position:absolute;left:93px;top:37px;font-size:10.5px;color:#fff}
.footer-links span{margin:0 5px;color:#ddd}
.copyright{position:absolute;left:895px;top:34px;font-size:10.5px;color:#fff}
</style>
</head>
<body>
<div class="page">
  <div class="abs brand"><span class="mark"></span>Redgum Skip Hire</div>

  <nav class="abs nav" style="left:0">
    <div class="nav-item" style="left:452px"><b>HOME</b><span>Back to home</span></div>
    <div class="nav-item" style="left:557px"><b>PRODUCT LIST</b><span>What we have for you</span></div>
    <div class="nav-item" style="left:705px"><b>DELIVERY AREA</b><span>Things we do</span></div>
    <div class="nav-item" style="left:862px"><b>CONTACT US</b><span>Ways to reach us</span></div>
  </nav>

  <div class="abs band"></div>
  <div class="abs slider" role="img" aria-label="Household rubbish and furniture piled up on a driveway ready for removal"></div>
  <div class="abs dots"><i class="dot"></i><i class="dot on"></i><i class="dot"></i><i class="dot"></i><i class="dot"></i></div>

  <h1 class="abs tagline" style="font-weight:400">Lorem ipsum dolor sit amet, consectetur adipisicing elit</h1>
  <div class="abs rule" style="top:540px"></div>

  <section class="abs tabs-box">
    <div class="tab-list">
      <div class="tab">Who we are?</div>
      <div class="tab active">Council permits</div>
      <div class="tab">What can you put in the bin?</div>
      <div class="tab" style="border:0">What can’t you put in the bin?</div>
    </div>
    <p class="tab-copy">A Council permit is required for bins placed outside your property i.e. on the road, nature strip or in a laneway/ROW. We will apply to Council for a permit on your behalf. Please call us for current permit rates for your area.</p>
    <div class="btn-more"><span>Learn More</span><span style="color:#999">····›</span></div>
    <div class="truck" role="img" aria-label="Skip delivery truck with loading crane"></div>
  </section>

  <div class="abs rule" style="top:847px"></div>

  <section class="abs social">
    <h2 class="col-title" style="font-weight:400">Social Connection</h2>
    <div class="follow">Follow Us On
      <span class="ico" style="background:#e0662a;margin-left:6px"></span>
      <span class="ico" style="background:#3b5da0"></span>
      <span class="ico" style="background:#c0302a"></span>
      <span class="ico" style="background:#3aa7c8"></span>
    </div>
  </section>

  <section class="abs newsletter">
    <h2 class="col-title">Newsletter</h2>
    <div class="field" style="margin-top:13px">your email address</div>
    <div class="btn-blue" style="margin-top:10px"><span>Subscribe</span><span>⟶</span></div>
  </section>

  <section class="abs touch">
    <h2 class="col-title" style="font-weight:400">Get In Touch</h2>
    <div class="field" style="margin-top:13px">your name</div>
    <div class="field" style="margin-top:7px">your email address</div>
    <div class="field" style="margin-top:7px;height:79px">message</div>
    <div class="btn-blue" style="margin-top:6px;margin-left:2px"><span>Send it</span><span>⟶</span></div>
  </section>

  <section class="abs contact">
    <h2 class="col-title" style="font-weight:400">Contact US</h2>
    <dl>
      <dd style="grid-column:1/3">12 Saltbush Road</dd>
      <dd style="grid-column:1/3">Kerrowvale Vic 3099</dd>
      <dt>Phone:</dt><dd>03 9000 1234</dd>
      <dt>Fax:</dt><dd>03 9000 5678</dd>
      <dt>Mobile:</dt><dd>0400 000 321</dd>
      <dt>E-mail:</dt><dd>hello@redgumskip.example.au</dd>
    </dl>
    <p class="accept">We accept Cash, Cheque, PayCard &amp; CardOne</p>
    <div class="cards"><div class="card">PayCard</div><div class="card">CardOne</div></div>
  </section>

  <footer class="abs footer">
    <div class="footer-links">Home<span>|</span>Product List<span>|</span>Delivery Area<span>|</span>Contact Us</div>
    <div class="copyright">Copyright</div>
  </footer>
</div>
</body>
</html>
```